Business Card Design

We are looking for a double sided business card.

On one side would be our logo

On the Other Side

Daniel Workby
Sales and Marketing

Phone/Text Logo and 530-471-6328
Email Logo and info@gildedcritters.example
Website Logo and www.gildedcritters.example
Facebook Logo and gilded critters
Instagram Logo and gilded_critters

Target Market(s)

Pet owners

Contact Information for Business Card

In project description

Requirements
Must have
• Logo

```html
<!DOCTYPE html>
<html lang="en">
<head>
<meta charset="utf-8">
<title>Gilded Critters – Business Card</title>
<link href="https://fonts.googleapis.com/css2?family=Montserrat:wght@400;500;700&display=swap" rel="stylesheet">
<style>
  :root {
    --stage: #3b3b3c;
    --card: #1b1b1b;
    --card-deep: #141414;
    --gold: #f6a41c;
    --gold-light: #ffc83a;
    --white: #f2f2f2;
    --muted: #d8d8d8;
  }
  * { box-sizing: border-box; margin: 0; padding: 0; }
  html, body { width: 1200px; height: 791px; overflow: hidden; }
  body {
    background: var(--stage);
    font-family: "Montserrat", Arial, sans-serif;
    position: relative;
  }
  .card {
    position: absolute;
    top: 247px;
    width: 520px;
    height: 297px;
    background: var(--card);
    box-shadow: 0 14px 30px rgba(0,0,0,.45);
    overflow: hidden;
  }
  .card--back { left: 50px; border-bottom: 2px solid var(--gold); border-right: 2px solid var(--gold); }
  .card--front { left: 630px; border: 2px solid var(--gold); }

  /* back side */
  .person { position: absolute; left: 44px; top: 182px; }
  .person__name {
    color: var(--gold-light);
    font-weight: 700;
    font-size: 21px;
    letter-spacing: .3px;
    text-transform: uppercase;
  }
  .person__role { color: var(--white); font-size: 15px; margin-top: 4px; }
  .divider {
    position: absolute;
    left: 262px; top: 92px;
    width: 1.5px; height: 112px;
    background: var(--gold);
  }
  .contacts { position: absolute; left: 282px; top: 86px; list-style: none; }
  .contacts li {
    display: flex; align-items: center; gap: 8px;
    color: var(--muted); font-size: 13.5px; line-height: 24px;
  }
  .contacts svg { width: 12px; height: 12px; flex: none; }

  /* front side */
  .pattern {
    position: absolute; inset: 0;
    background: radial-gradient(ellipse at 70% 40%, #2c2c2c 0%, var(--card-deep) 70%);
  }
  .brand {
    position: absolute; inset: 0;
    display: flex; flex-direction: column; align-items: center; justify-content: center;
  }
  .brand__name {
    color: var(--white);
    font-weight: 700;
    font-size: 40px;
    letter-spacing: 1px;
    text-transform: uppercase;
  }
  .brand__url {
    margin-top: 14px;
    color: var(--gold);
    font-weight: 500;
    font-size: 12px;
    letter-spacing: 3px;
    text-transform: uppercase;
  }
</style>
</head>
<body>

<section class="card card--back" aria-label="Business card, contact side">
  <div class="person">
    <p class="person__name">Daniel Workby</p>
    <p class="person__role">Sales and Marketing</p>
  </div>
  <div class="divider"></div>
  <ul class="contacts">
    <li>
      <svg viewBox="0 0 12 12" aria-hidden="true"><path fill="#f6a41c" d="M2.5 1l2 .3.8 2.4-1.2 1a6.5 6.5 0 0 0 3 3l1-1.2 2.4.8.3 2A1.5 1.5 0 0 1 9.3 11 8.5 8.5 0 0 1 1 2.7 1.5 1.5 0 0 1 2.5 1z"/></svg>
      530-471-6328
    </li>
    <li>
      <svg viewBox="0 0 12 12" aria-hidden="true"><rect x="1" y="2.5" width="10" height="7" rx="1" fill="#f6a41c"/><path d="M1.5 3l4.5 3.5L10.5 3" stroke="#1b1b1b" stroke-width="1" fill="none"/></svg>
      info@gildedcritters.example
    </li>
    <li>
      <svg viewBox="0 0 12 12" aria-hidden="true"><circle cx="6" cy="6" r="5" fill="none" stroke="#f6a41c" stroke-width="1.2"/><ellipse cx="6" cy="6" rx="2.2" ry="5" fill="none" stroke="#f6a41c" stroke-width="1"/><path d="M1 6h10" stroke="#f6a41c" stroke-width="1"/></svg>
      www.gildedcritters.example
    </li>
    <li>
      <svg viewBox="0 0 12 12" aria-hidden="true"><rect x="1" y="1" width="10" height="10" rx="2" fill="#f6a41c"/></svg>
      gilded critters
    </li>
    <li>
      <svg viewBox="0 0 12 12" aria-hidden="true"><circle cx="6" cy="6" r="5" fill="#f6a41c"/></svg>
      gilded_critters
    </li>
  </ul>
</section>

<section class="card card--front" aria-label="Business card, brand side">
  <div class="pattern" role="img" aria-label="Repeating glossy brand mark pattern across the card background"></div>
  <div class="brand">
    <p class="brand__name">Gilded Critters</p>
    <p class="brand__url">www.gildedcritters.example</p>
  </div>
</section>

</body>
</html>
```